Verpackungen für Temperatur-Kalibrierprodukte
Zielgruppe
Wir sind eine Firma, die Temperatur-Kalibrierprodukte vertreibt und suchen ein hochwertiges Design für die Verpackung unserer High-End Thermometer. Unsere Zielgruppe sind Firmen aus Industrie, Forschung und Entwicklung.
Aufgabenstellung
Wir suchen ein Design für eine Magnetbox, in der unsere hochwertigen Thermometer transportiert und aufbewahrt werden. Das Design soll sich an unsere Website-Gestaltung anlehnen, bzw. dazu passen.
Auf die Verpackung sollte das Logo, sowie das Wort 'Präzisionsthermometer'.
Innenmaße der Verpackung:
60 x 13 x 4,5 / 4,5 cm (Breite x Tiefe x Höhe/Klappenhöhe)
Material: 1,8 mm Graubpappe innen weiß
Bezugsmaterial: außen weißes Kraftpapier 157g
Bei Bedarf können wir weiteres Bildmaterial zur Verfügung stellen (siehe Website).

```html
<!DOCTYPE html>
<html lang="de">
<head>
<meta charset="utf-8">
<title>Thermavo Magnetbox – Stanzbogen</title>
<link rel="stylesheet" href="https://fonts.googleapis.com/css2?family=Montserrat:wght@400;700&display=swap">
<style>
  :root {
    --canvas: #cccccc;
    --board: #ffffff;
    --cut-line: #5a5a5a;
    --brand-ink: #1c1c1c;
    --brand-dot: #3b3b3b;
    --band-deep: #7e1c22;
    --band-light: #e27c80;
    --band-text: #ffffff;
  }
  html, body {
    margin: 0;
    padding: 0;
    width: 1200px;
    height: 960px;
    overflow: hidden;
    background: var(--canvas);
  }
  .dieline {
    display: block;
    width: 1200px;
    height: 960px;
  }
  .panel, .flap {
    fill: var(--board);
    stroke: var(--cut-line);
    stroke-width: 0.7;
  }
  .brand-name {
    font-family: "Montserrat", sans-serif;
    font-weight: 700;
    fill: var(--brand-ink);
  }
  .brand--small .brand-name { font-size: 24px; }
  .brand--large .brand-name { font-size: 40px; }
  .brand-dot { fill: var(--brand-dot); }
  .band-label {
    font-family: "Montserrat", sans-serif;
    font-size: 17px;
    fill: var(--band-text);
    letter-spacing: 0.3px;
  }
  .band-label .light { font-weight: 400; }
  .band-label .bold { font-weight: 700; }
</style>
</head>
<body>
<svg class="dieline" viewBox="0 0 1200 960" xmlns="http://www.w3.org/2000/svg">
  <defs>
    <linearGradient id="ribbon-sheen" x1="192" y1="610" x2="1008" y2="686" gradientUnits="userSpaceOnUse">
      <stop offset="0" stop-color="var(--band-deep)"/>
      <stop offset="0.17" stop-color="var(--band-light)"/>
      <stop offset="0.33" stop-color="var(--band-deep)"/>
      <stop offset="0.5" stop-color="var(--band-deep)"/>
      <stop offset="0.68" stop-color="var(--band-deep)"/>
      <stop offset="0.8" stop-color="var(--band-light)"/>
      <stop offset="1" stop-color="var(--band-deep)"/>
    </linearGradient>
    <filter id="band-shadow" x="-5%" y="-50%" width="110%" height="200%">
      <feDropShadow dx="0" dy="4" stdDeviation="3" flood-color="#000" flood-opacity="0.22"/>
    </filter>
  </defs>

  <!-- side flaps -->
  <g class="side-flap side-flap--left">
    <polygon class="flap" points="135.3,257.7 186.5,257.7 192,272.7 130.8,272.7"/>
    <rect class="flap" x="130.8" y="272.7" width="61.2" height="176.5"/>
    <polygon class="flap" points="130.8,449.2 192,449.2 186.5,464.5 135.3,464.5"/>
  </g>
  <g class="side-flap side-flap--right">
    <polygon class="flap" points="1013.5,257.7 1064.7,257.7 1069.2,272.7 1008,272.7"/>
    <rect class="flap" x="1008" y="272.7" width="61.2" height="176.5"/>
    <polygon class="flap" points="1008,449.2 1069.2,449.2 1064.7,464.5 1013.5,464.5"/>
  </g>

  <!-- lid flap -->
  <rect class="panel" x="192" y="211.5" width="816" height="61.2"/>
  <g class="brand brand--small" transform="translate(600 242)">
    <circle class="brand-dot" cx="-67" cy="0" r="13"/>
    <text class="brand-name" x="-47" y="9">Thermavo</text>
  </g>

  <!-- lid top -->
  <rect class="panel" x="192" y="272.7" width="816" height="176.5"/>

  <!-- back panel (upside down) -->
  <rect class="panel" x="192" y="449.2" width="816" height="61.2"/>
  <g class="brand brand--small" transform="translate(600 479) rotate(180)">
    <circle class="brand-dot" cx="-67" cy="0" r="13"/>
    <text class="brand-name" x="-47" y="9">Thermavo</text>
  </g>

  <!-- front panel -->
  <rect class="panel" x="192" y="510.4" width="816" height="177"/>
  <g class="brand brand--large" transform="translate(600 573)">
    <circle class="brand-dot" cx="-110" cy="0" r="22"/>
    <text class="brand-name" x="-79" y="14">Thermavo</text>
  </g>
  <g class="product-band" filter="url(#band-shadow)">
    <rect x="192" y="629.5" width="816" height="36.7" fill="url(#ribbon-sheen)"/>
  </g>
  <text class="band-label" x="600" y="654" text-anchor="middle"><tspan class="light">PRÄZISIONS</tspan><tspan class="bold">THERMOMETER</tspan></text>

  <!-- bottom flap -->
  <rect class="panel" x="192" y="687.4" width="816" height="61.2"/>
  <g class="brand brand--small" transform="translate(600 718)">
    <circle class="brand-dot" cx="-67" cy="0" r="13"/>
    <text class="brand-name" x="-47" y="9">Thermavo</text>
  </g>
</svg>
</body>
</html>
```